Ridgeline Outfitters Business Cards

Recently had a logo done with Artflockr and now looking for a business card to go along with it.

Target Market(s)

Ridgeline Outfitters is a weapons dealer. My market will be primarily men, hunting, shooting type.

Industry/Entity Type

Business

Contact Information for Business Card

I selected double sided, but this is not required, single or double is going to be fine. I picture the logo on one side, or perhaps just the circle which contains "RO" with the remaining info on the other side.

Font styles to use
Sans Serif

Requirements
Must have
• My name: Wesley Holm
• Title: Owner
• tel: 612-555-0378
• web: www.ridgelineoutfittersmn.example
Nice to have
• I like the concept of a black business card. I would like to keep the colors monotone, black, grey, white or red. Red is acceptable because it is in the logo. I have also seen cards that are matte black with shiny black as well, perhaps for the logo (or circle RO) part of the logo.
• I will upload a couple of the logos for use, and also an example I just found of the black on black. and some others that have a nice contrast.
Should not have
• lots of colors are not wanted.

```html
<!DOCTYPE html>
<html lang="en">
<head>
<meta charset="utf-8">
<title>Ridgeline Outfitters Business Cards</title>
<link rel="stylesheet" href="https://fonts.googleapis.com/css2?family=Montserrat:wght@400;500;600&display=swap">
<style>
  :root {
    --bg: #e9e6e1;
    --card-black: #232322;
    --card-white: #f4f4f3;
    --red: #e0242c;
    --grey: #5b5b5d;
    --grey-dark: #3a3a3a;
    --ink: #3a3a3c;
  }
  * { margin: 0; padding: 0; box-sizing: border-box; }
  html, body {
    width: 1200px; height: 801px; overflow: hidden;
    background: var(--bg);
    font-family: "Montserrat", sans-serif;
  }
  .sheet { position: relative; width: 1200px; height: 801px; }
  .card {
    position: absolute; left: 320px;
    width: 560px; height: 320px;
    border-radius: 4px;
    box-shadow: 0 6px 18px rgba(0,0,0,.12);
  }
  .card--back { top: 50px; background: var(--card-black); }
  .card--front { top: 430px; background: var(--card-white); }

  .brand {
    position: absolute; inset: 0;
    display: flex; align-items: center; justify-content: center; gap: 20px;
  }
  .brand__dot {
    width: 64px; height: 64px; border-radius: 50%;
    background: var(--grey-dark); flex: none;
  }
  .brand__name {
    color: var(--red); font-weight: 600; font-size: 26px;
    letter-spacing: 3px; text-transform: uppercase;
  }

  .front-brand {
    position: absolute; left: 40px; top: 0; bottom: 0; width: 180px;
    display: flex; align-items: center;
  }
  .front-brand__name {
    color: var(--red); font-weight: 600; font-size: 22px;
    line-height: 1.25; letter-spacing: 1px; text-transform: uppercase;
  }

  .contact { position: absolute; left: 250px; top: 96px; color: var(--ink); }
  .contact__name { font-size: 26px; font-weight: 500; color: var(--grey); }
  .contact__title { font-size: 14px; font-weight: 500; color: var(--red); margin-top: 2px; }
  .contact__list { list-style: none; margin-top: 18px; }
  .contact__item {
    display: flex; align-items: center; gap: 10px;
    font-size: 13px; font-weight: 500; color: var(--ink);
    margin-bottom: 9px; white-space: nowrap;
  }
  .contact__icon { width: 14px; height: 14px; flex: none; }
</style>
</head>
<body>
<main class="sheet">
  <section class="card card--back" aria-label="Card back">
    <div class="brand">
      <span class="brand__dot"></span>
      <span class="brand__name">Ridgeline Outfitters</span>
    </div>
  </section>

  <section class="card card--front" aria-label="Card front">
    <div class="front-brand">
      <p class="front-brand__name">Ridgeline<br>Outfitters</p>
    </div>
    <div class="contact">
      <p class="contact__name">Wesley Holm</p>
      <p class="contact__title">Owner</p>
      <ul class="contact__list">
        <li class="contact__item">
          <svg class="contact__icon" viewBox="0 0 16 16"><path fill="#e0242c" d="M3.5 1.5l2.5 3-1.5 1.8c.9 1.9 2.3 3.3 4.2 4.2L10.5 9l3 2.5-1.2 2.6C6.6 13.6 2.4 9.4 1.9 3.7z"/></svg>
          612-555-0378
        </li>
        <li class="contact__item">
          <svg class="contact__icon" viewBox="0 0 16 16"><rect x="1" y="3" width="14" height="10" rx="1" fill="#e0242c"/><path d="M1.5 3.5L8 9l6.5-5.5" stroke="#f4f4f3" stroke-width="1.3" fill="none"/></svg>
          hello@ridgelineoutfitters.example
        </li>
        <li class="contact__item">
          <svg class="contact__icon" viewBox="0 0 16 16" fill="none" stroke="#e0242c" stroke-width="1.3"><circle cx="8" cy="8" r="6.3"/><ellipse cx="8" cy="8" rx="2.7" ry="6.3"/><path d="M1.7 8h12.6M2.8 4.8h10.4M2.8 11.2h10.4"/></svg>
          www.ridgelineoutfittersmn.example
        </li>
      </ul>
    </div>
  </section>
</main>
</body>
</html>
```